wedding invitation (invitation + save the date card)
Marcella&Joost
Dear MarJoo,
I have uploaded the draft#23,#24 please check and give comments.
@tintapress, draft #22,
Thanks for your modifications! We're very happy with the design.
Just a few thing we would like to try
- The palace icon in the right inside page is great. Can we change the color to one we've already used, like orange or green?
- We were thinking that maybe all the pages green is a bit too much, can you try to see what happens if we make the background of the right inside page white instead of yellow?
- just to check: you're sending us the complete photoshop file with all the layers right? So if we later would like to change the text we can do it ourselves, right?
Have fun making the last modifications!
@redwave, draft #19,
Thanks for your new draft. We see that you've added some color and made the line illustrating the face of Urbino lighter. Please use the feedback provided to elaborate. Thanks for the hard work.
@pelsa, draft #20,
Thanks for your new draft. We like what you've did with the sunflower and tulip.
The blue-greenish color is not our favourite, it doesn't respond to Holland or Italy for us.
Although we like that you've kept the design simple, it's a bit too simple for us. Please use the feedback provided and keep on elaborating.
@tintapress, draft #21
Well done, we really like what you've made!
Backside:
- the tulip and the sunflower are close to perfect. The only thing we would like to try out is to see what happens if you design the tulip open. Now it's like a blossem.
- The ribbon with written Sposi on top we don't like so much, it's too romantic. We do like the leaf and hart in the top left corner. The sunflower and tulip are beautifull enough, we don't think they need the ribbon, etc.
Front:
- Great what you did with the photos, how you've written Marcella&Joost and the sunflower/tulip.
- Like on the backside, the ribbon we don't like as much. Could you remove the ribbon, the word Sposi and the two little flowers and the little leaf. The bigger flower and bigger leaf in the bottom right corner can stay. Maybe the part below the photo gets too white?? Maybe you could put the hart, birds and rings which are next to the tulip, to the part below the photos??
Inside Left:
- We really like what you've did with the photo of Urbino, it looks great. Also how you've put down the details of our masters of ceremony is great.
- Do you see a way of showing more the two little towers of the palace (right)? Maybe instead of the cathedral (left).
- Also here the ribbon we don't like as much, and also the phrase Our Wedding at Urbino is strange because it's in English. We do agree though that the top right corner needs a little decoration. Maybe you could take away the ribbon, the words and just leave a couple of flowers and leafes??
Inside Right:
- In general is great how you've designed it! Great.
- The little circles around the tulip and sunflowers, we don't know what they are and seem to us a bit crowed, maybe you can leave them off?
- We like what you've did with the shape of the cathedral, but since we're not getting married in a church, maybe you could do the same thing but use the two distinct little towers of the palace? We would also prefer you to leave away the ribbon.
Small card:
- Great work, just a little busy. Maybe you could leave the white circle, hart, 3 flowers and 2 leafes from the center. And also the circles around the sunflower and tulip.
@all
We've given the text some thought, this is what we would like:
- Front page: no text, just Joost & Marcella, the 3 photos and some tulips and sunflowers.
- First middle page: Maestri di cerimonia
Ceremoniemeesters
Maarten Vloskamp: +31 6 5807 3926 maarten.vloskamp@voorbeeldnet.com
Loredana Ferrucci: +39 347 582 9061 Loredana.Ferrucci@esempiorete.it
RSVP via e-mail: Marcella.Joost@esempiorete.it
This together with the face of the city of Urbino.
- Second middle page: Joost Hendriks & Marcella Tommasini
Ci Sposiamo!
Gaan Trouwen!
18 Giugno 2011, ore 16:00
Comune di Urbino
18 juni 2011, 16:00uur
Dopo la cerimonia facciamo un brindisi al bar ‘la lanterna’
Na de ceremonie brengen we een toost uit in de bar ‘la lanterna’
Maybe white letters at a colored background?? Here also some tulips and sunflowers.
-Rear page: Joost & Marcella
Via Ludovico Sanzetti 14
61029 Urbino (PU) Italia
Marcella.Joost@esempiorete.it
-inlay page (for the special invites, transparant): Saremo lieti di festeggiare il nostro matrimonio insieme a voi!
We willen ons huwelijk graag met jou vieren!
Ore 18:30 circa
18:30uur circa
Ca’ Ferrona
Località Ca’Ferrona, Fermignano
Maybe without any designs or just one tulip and sunflower in a corner.
@sandquill, draft #18,
We like a lot that you've used the Kwast Utrecht cards as inspiration. -
- The tulips and the city of Urbino we really like!!
- The sunflowers we don't like as much, they're too big and they are too many. Also the idea of the photos in the sunflowers we don't like as much. Maybe you could try to make a sunflower designed like the tulips. I imagine like a bouquet of tulips and sunflowers.
- The letters of the formal text we prefer in a normal font like arial, so lighter and less playfull. We think it could balance nicely the serious card with playfull designs.
- We like the idea of a self mailer, but prefer a normal card that opens like a book. With a front, two pages on the inside and a rear. On the front we would like to see 'our story', the middle pages: the left one for Urbino (with maybe the addresses of the masters of ceremony) and right one for the formal text in 2 languages (dutch and Italian). On the back we'd like to put our addresses.
- The envelope will probably be a standard size, square envelope. Maybe even transparant/opaque.
Thanks for your design, keep on elaborating!
@Tintapress, #15,
Thanks for your draft, it looks very professional.
- We like the flowers! Although we were looking for something more like a scetch, drawing.
- The 3 photos on the front we like. Could you maybe give them just a little bit of color?
- The idea of the photo of Urbino is great. What happens if you put the photo on one face of the card full size?
- How do you see the information we have to put in the card, where will it come?
Thanks, keep on elaborating!
@pelsa, draft #12,
Although is difficult to see, because the image is rather small, we like a lot the tulip and the sunflower. It seems drawn with the hand, that's the stile we like! Please continue based on the feedback we've posted! Thanks
@Pix4lWorks, Draft #4
Thanks for your draft. We like how you wrote Joost & Marcella. Please continu based on the comments posted. Thanks
@Redwave, draft #1, #2, #3, #6, #7, #8, #9, #13,
Thanks for the hard work, you've been very productive. Keep up the good work and keep elaborating.
- The 3 photos in the front we like all in the same size, like you did in #13.
- The line showing the palace of Urbino is nice. We would like to see more as a line of a pencil, like someone drew it on the card. It may also be smaller, more subtle (sottile), delicate.
- The flowers we don't like as much, we're looking more for something less computerish, less perfect, more like a scetch, drawn with the hand. like the card on the following link: http://www.kaartvoorbeeld.nl/kaarten.php?id=52807&naam=ZomerGroet

```html
<!DOCTYPE html>
<html lang="it">
<head>
<meta charset="utf-8">
<title>Marcella &amp; Joost – wedding stationery</title>
<link rel="stylesheet" href="https://fonts.googleapis.com/css2?family=Open+Sans:wght@400;600;700&display=swap">
<style>
:root{
  --canvas:#dedede;
  --paper:#ffffff;
  --inlay:#f3f3f3;
  --butter:#fcf7c4;
  --ink:#1d1d1d;
  --monogram:#6d6a22;
  --fold:#b9b9b9;
  --bloom-a:#e8c77a;
  --bloom-b:#b9c07a;
  --city-a:#fbe7bd;
  --city-b:#f1c98a;
  --photo-a:#5d5853;
  --photo-b:#a9a19a;
}
*{box-sizing:border-box;margin:0;padding:0}
html,body{width:1200px;height:931px;overflow:hidden}
body{background:var(--canvas);position:relative;font-family:"Open Sans",Arial,sans-serif;color:var(--ink)}
.sheet{position:absolute;background:var(--paper);overflow:hidden}
.band{position:absolute;left:0;width:100%;background:var(--butter)}
.fold{position:absolute;top:0;bottom:0;left:387px;border-left:1px dashed var(--fold)}
.panel{position:absolute;top:0;bottom:0}
.monogram{position:absolute;left:0;right:0;text-align:center;font-weight:600;font-size:19px;line-height:24px;color:var(--monogram);letter-spacing:.5px;white-space:nowrap}
.bouquet{position:absolute;border-radius:8px;background:linear-gradient(180deg,var(--bloom-a),var(--bloom-b))}
.cityscape{position:absolute;border-radius:4px;background:linear-gradient(180deg,var(--city-a),var(--city-b))}
.photo{position:absolute;top:0;height:100%;background:linear-gradient(135deg,var(--photo-a),var(--photo-b))}
.copy{position:absolute;font-size:10px;font-weight:600;line-height:15px;white-space:nowrap}
.copy.center{text-align:center}
.copy p{min-height:15px}
</style>
</head>
<body>

<section class="sheet cover" style="left:8px;top:8px;width:780px;height:402px">
  <div class="band" style="top:0;height:231px"></div>
  <div class="fold"></div>

  <div class="panel rear" style="left:0;width:387px">
    <div class="monogram" style="top:252px">Marcella &amp; Joost</div>
    <div class="copy" style="left:148px;top:290px">
      <p>Via Ludovico Sanzetti 14</p>
      <p>61029 Urbino (PU) Italia</p>
      <p>+31 6 5807 3926 / +39 347 582 9061</p>
      <p>Marcella.Joost@esempiorete.it</p>
    </div>
  </div>

  <div class="panel front" style="left:388px;width:392px">
    <div class="photos" style="position:absolute;left:5px;right:0;top:73px;height:80px">
      <div class="photo" role="img" aria-label="Photo of the couple on a scooter" style="left:0;width:126px"></div>
      <div class="photo" role="img" aria-label="Photo of the couple together" style="left:128px;width:128px;filter:brightness(.8)"></div>
      <div class="photo" role="img" aria-label="Photo of the couple smiling" style="left:258px;width:129px;filter:brightness(1.1)"></div>
    </div>
    <div class="bouquet" role="img" aria-label="Hand-drawn bouquet of tulips and sunflowers" style="left:166px;top:250px;width:60px;height:92px"></div>
    <div class="monogram" style="top:354px">Marcella &amp; Joost</div>
  </div>
</section>

<section class="sheet inlay" style="left:800px;top:8px;width:393px;height:402px;background:var(--inlay)">
  <div class="copy center" style="left:0;right:0;top:66px">
    <p>Saremo lieti di festeggiare il nostro matrimonio insieme a voi!</p>
    <p>We willen ons huwelijk graag met jou vieren!</p>
    <p></p>
    <p>Ore 18:30 circa</p>
    <p>18:30uur circa</p>
    <p>Ca’ Ferrona</p>
    <p>Località Ca’Ferrona, Fermignano</p>
  </div>
  <div class="bouquet" role="img" aria-label="Hand-drawn bouquet of tulips and sunflowers" style="left:166px;top:228px;width:60px;height:92px"></div>
  <div class="monogram" style="top:331px">Marcella &amp; Joost</div>
</section>

<section class="sheet inside" style="left:8px;top:423px;width:780px;height:495px">
  <div class="fold"></div>

  <div class="panel ceremony" style="left:0;width:387px">
    <div class="copy center" style="left:0;right:0;top:45px">
      <p>Maestri di Cerimonia</p>
      <p>Ceremoniemeesters</p>
      <p></p>
      <p>Maarten Vloskamp: +31 6 5807 3926</p>
      <p>maarten.vloskamp@voorbeeldnet.com</p>
      <p></p>
      <p>Loredana Ferrucci: +39 347 582 9061</p>
      <p>Loredana.Ferrucci@esempiorete.it</p>
      <p></p>
      <p>RSVP via e-mail: Marcella.Joost@esempiorete.it</p>
    </div>
    <div class="cityscape" role="img" aria-label="Sketch of the Urbino skyline with the palace towers" style="left:32px;top:260px;width:322px;height:88px"></div>
  </div>

  <div class="panel formal" style="left:388px;width:392px">
    <div class="bouquet" role="img" aria-label="Hand-drawn bouquet of tulips and sunflowers" style="left:166px;top:14px;width:60px;height:92px"></div>
    <div class="copy center" style="left:0;right:0;top:122px">
      <p>Joost Hendriks &amp; Marcella Tommasini</p>
      <p></p>
      <p>Ci Sposiamo!</p>
      <p>Gaan Trouwen!</p>
      <p></p>
      <p>18 Giugno 2011, ore 16:00</p>
      <p>Comune di Urbino</p>
      <p>18 juni 2011, 16:00uur</p>
      <p></p>
      <p>Dopo la cerimonia facciamo un brindisi al bar ‘la lanterna’</p>
      <p>Na de ceremonie brengen we een toost uit in de bar ‘la lanterna’</p>
    </div>
  </div>
</section>

<section class="sheet save-the-date" style="left:800px;top:423px;width:393px;height:495px">
  <div class="band" style="top:0;height:236px"></div>
  <div class="bouquet" role="img" aria-label="Hand-drawn bouquet of tulips and sunflowers" style="left:72px;top:70px;width:48px;height:100px"></div>
  <div class="monogram" style="top:152px;left:128px;right:auto;width:200px">Marcella &amp; Joost</div>
  <div class="copy center" style="left:0;right:0;top:292px">
    <p>Segnatevi questa data e non mancate</p>
    <p>18 Giugno 2011 | 18 juni 2011</p>
    <p></p>
    <p>Ci Sposiamo!</p>
    <p>Gaan Trouwen!</p>
    <p></p>
    <p>Invito formale a seguire</p>
  </div>
  <div class="cityscape" role="img" aria-label="Sketch of the Urbino skyline with the palace towers" style="left:12px;top:398px;width:246px;height:88px"></div>
</section>

</body>
</html>
```